Updated Stationary needed using new logo for Hair Tissue Mineral Analysis Company

Simple stationary design needed using new logo!
1. 8.5" x 11" Letterhead with company information listed below
2. 8.5" x 11" Design with Footer only with logo and information for print materials
3. 5.5" x 8.5" letterhead design
4. 4.125" x 9.5" Business envelope (#10 envelope) with address
5. 4.125" x 9.5" Business envelope with clear window (#10 envelope) with address
6. 6.5" x 9.5" envelope (6 3/4 Booklet envelope) with address
7. 10" x 13" Open End envelope
Address:
4817 N. Corwin Street
Phoenix, AZ 85021
Phone:
(602)-417-3926
Website:
www.pexumor.com
Email:
information@pexumor.com
Updates
Need extra days to review
Focused on completing other projects first
Look and feel
Each slider illustrates characteristics of the customer's brand and the style your logo design should communicate.

```html
<!DOCTYPE html>
<html lang="en">
<head>
<meta charset="utf-8">
<title>Pexumor Labs Letterhead</title>
<link rel="stylesheet" href="https://fonts.googleapis.com/css2?family=Lato:wght@400;700&family=Montserrat:wght@400;500&display=swap">
<style>
  :root {
    --bg: #e2e2e2;
    --paper: #ffffff;
    --brand-blue: #2d57a0;
    --brand-orange: #f28a1d;
    --navy: #1f3a5c;
    --ink: #111111;
    --body-text: #7a7a7a;
    --muted: #7d7d7d;
    --rule: #a9a9a9;
    --sig-tone: #dcdcdc;
  }
  * { margin: 0; padding: 0; box-sizing: border-box; }
  html, body { width: 1154px; height: 1200px; overflow: hidden; background: var(--bg); }
  .letterhead {
    position: absolute; left: 113px; top: 0;
    width: 927px; height: 1200px;
    background: var(--paper);
    font-family: "Lato", Arial, sans-serif;
  }
  .brand {
    position: absolute; top: 62px; left: 0; width: 100%;
    display: flex; justify-content: center; align-items: center; gap: 12px;
  }
  .brand-dot { width: 22px; height: 22px; border-radius: 50%; background: var(--brand-orange); }
  .brand-name { font-size: 34px; font-weight: 700; color: var(--brand-blue); letter-spacing: 0.5px; }
  .recipient { position: absolute; left: 86px; top: 250px; }
  .recipient-name { font-size: 18.5px; font-weight: 700; color: var(--navy); }
  .recipient-title { font-size: 13px; font-weight: 700; color: var(--ink); margin-top: 4px; }
  .letter-date { position: absolute; right: 87px; top: 273px; font-size: 13.5px; color: var(--muted); }

  .letter-content {
    position: absolute; left: 87px; top: 339px; width: 754px;
    display: flex; flex-direction: column; align-items: flex-start;
  }
  .letter-body { width: 100%; }
  .letter-body p {
    font-size: 13.8px; line-height: 21.9px; color: var(--body-text);
    text-align: justify; hyphens: auto; margin-bottom: 21.9px;
  }
  .letter-body p:last-child { margin-bottom: 0; }
  .signature {
    width: 196px; height: 42px; margin-top: 52px;
    background: linear-gradient(90deg, var(--sig-tone), #eeeeee); border-radius: 4px;
  }
  .signer { margin-top: 24px; }
  .signer-name { font-size: 17.5px; font-weight: 700; color: var(--ink); }
  .signer-title { font-size: 13.5px; font-weight: 700; color: var(--muted); margin-top: 4px; }

  .footer-rule { position: absolute; left: 86px; right: 86px; top: 1131px; height: 2px; background: var(--rule); }
  .contact-bar {
    position: absolute; left: 86px; right: 86px; top: 1148px;
    display: flex; justify-content: center; align-items: center; gap: 7px;
    font-family: "Montserrat", Arial, sans-serif; font-size: 13.2px; color: var(--ink); white-space: nowrap;
  }
  .contact-item { display: flex; align-items: center; gap: 4px; }
  .contact-item svg { width: 13px; height: 13px; fill: var(--brand-orange); flex: none; }
</style>
</head>
<body>
<main class="letterhead">
  <header class="brand">
    <span class="brand-dot"></span>
    <span class="brand-name">Pexumor Labs</span>
  </header>

  <section class="recipient">
    <div class="recipient-name">Dear. Mrs Dana Whitlow</div>
    <div class="recipient-title">Chief Director</div>
  </section>
  <div class="letter-date">Date: 07-August-2025</div>

  <section class="letter-content">
    <div class="letter-body">
      <p>Lorem ipsum dolor sit amet, consectetur adipiscing elit, sed do eiusmod tempor incididunt ut labore et dolore magna aliqua. Sollicitudin ac orci phasellus egestas tellus rutrum tellus. Euismod elementum nisi quis eleifend quam adipiscing vitae proin sagittis. Egestas sed tempus urna et pharetra pharetra. Quis blandit turpis cursus in hac habitasse. Sed velit dignissim sodales ut eu. Ac auctor augue mauris augue neque. In arcu cursus euismod quis viverra nibh cras pulvinar mattis. Libero justo laoreet sit amet. Felis eget nunc lobortis mattis aliquam faucibus purus in. Pulvinar etiam non quam lacus suspendisse faucibus. Odio tempor orci dapibus ultrices. Velit dignissim sodales ut eu sem integer vitae justo. Fermentum et sollicitudin ac orci phasellus egestas. Pharetra vel turpis nunc eget lorem dolor sed. Sed turpis tincidunt id aliquet risus feugiat in ante. Mus mauris vitae ultricies leo integer malesuada nunc vel. Rhoncus urna neque viverra justo nec ultrices dui. Ut placerat orci nulla pellen&shy;tesque dignissim enim sit amet.</p>
      <p>Bibendum arcu vitae elementum curabitur vitae nunc. Nunc pulvinar sapien et ligula ullamcorper malesuada. At elementum eu facilisis sed. Erat pellentesque adipiscing commodo elit at imperdiet dui accumsan sit. Nunc scelerisque viverra mauris in aliquam sem fringilla. In vitae turpis massa sed. Volutpat ac tincidunt vitae semper quis lectus nulla at. Massa placerat duis ul&shy;tricies lacus sed turpis. Dui vivamus arcu felis bibendum ut tristique et egestas. Blandit aliquam etiam erat velit scelerisque in dictum non consectetur. Id neque aliquam vestibulum morbi blandit cursus risus at. Sed egestas egestas fringilla phasellus faucibus scelerisque eleifend donec. Ornare quam viverra orci sagittis eu volutpat odio facilisis. Volutpat sed cras ornare arcu dui vivamus arcu. Interdum consectetur libero id faucibus nisl.</p>
      <p>Viverra mauris in aliquam sem. Mattis molestie a iaculis at erat pellentesque adipiscing commodo elit. Sit amet volutpat con&shy;sequat mauris nunc. Aliquam nulla facilisi cras fermentum. Sed turpis tincidunt id aliquet risus feugiat. Augue neque gravida in fermentum et sollicitudin ac orci.</p>
    </div>

    <div class="signature" role="img" aria-label="Handwritten signature of Robert Calloway"></div>
    <div class="signer">
      <div class="signer-name">Robert Calloway</div>
      <div class="signer-title">Chief Director</div>
    </div>
  </section>

  <div class="footer-rule"></div>
  <footer class="contact-bar">
    <span class="contact-item">
      <svg viewBox="0 0 24 24"><path d="M6.6 10.8a15.1 15.1 0 0 0 6.6 6.6l2.2-2.2c.3-.3.7-.4 1-.2 1.1.4 2.3.6 3.6.6.6 0 1 .4 1 1V20c0 .6-.4 1-1 1A17 17 0 0 1 3 4c0-.6.4-1 1-1h3.5c.6 0 1 .4 1 1 0 1.3.2 2.5.6 3.6.1.3 0 .7-.2 1z"/></svg>
      (602)-417-3926
    </span>
    <span class="contact-item">
      <svg viewBox="0 0 24 24"><path d="M2 5h20v14H2z M2 5l10 8 10-8"/></svg>
      information@pexumor.com
    </span>
    <span class="contact-item">
      <svg viewBox="0 0 24 24"><circle cx="12" cy="12" r="10"/></svg>
      www.pexumor.com
    </span>
    <span class="contact-item">
      <svg viewBox="0 0 24 24"><path d="M12 2a7 7 0 0 0-7 7c0 5.2 7 13 7 13s7-7.8 7-13a7 7 0 0 0-7-7zm0 9.5a2.5 2.5 0 1 1 0-5 2.5 2.5 0 0 1 0 5z"/></svg>
      4817 N. Corwin Street, Phoenix, AZ 85021
    </span>
  </footer>
</main>
</body>
</html>
```